Harlow Ironworks Business Card

We need a business card design for a new small metal fabrication business in rural NSW, Australia.

The business (Harlow Ironworks) is owner operated by a man with the initials KB - much of the branding comes from this name.

Harlow Ironworks designs, engineers, repairs and manufactures a range of custom, quality metal works including vehicle trays, agricultural machinery impliments, trailers, wood splitters, fire pits, furniture etc.

The brand position focuses on custom work of the highest quality.

Business card design should show quality, attention to detail and stand out among a mass of business cards.

Logos are in the files

The grey color may be changed on the logo if required to stand out more.

There is an image attached of a simple card that is liked because it is clean, clear, simple, masculine and effective. It says 'quality'. As most of the work we do is custom it would be good to have the business card speak to this.

Target Market(s)

Rural and regional based Australians. Primarily adult male 25-60 yrs. Primary production / rural / travelling lifestyle.

Industry/Entity Type

Metal Fabrication

Contact Information for Business Card

The words 'custom quality fabrications' would be great somewhere perhaps on the backside (not on the information side)
Name
title
Phone: 0418 539 746 and (02) 6193 4827
email: info@harlowiw.com.au
www.harlowiw.com.au

address (2 lines)

Requirements
Nice to have
• Background colour should be very navy blue or black.
Should not have
• NO orange and blue combinations.
• Navy is OK

```html
<!DOCTYPE html>
<html lang="en">
<head>
<meta charset="utf-8">
<title>Harlow Ironworks Business Card</title>
<link rel="stylesheet" href="https://fonts.googleapis.com/css2?family=Arimo:ital,wght@0,400;0,700;1,400&display=swap">
<style>
  :root {
    --page: #ffffff;
    --card-white: #ffffff;
    --card-black: #0b0d0e;
    --accent-red: #ff0a00;
    --brand-grey: #a7a9ac;
    --brand-green: #66e01e;
    --text-light: #ffffff;
    --text-soft: #d9d9d9;
  }
  html, body {
    margin: 0;
    padding: 0;
    width: 1200px;
    height: 1200px;
    overflow: hidden;
    background: var(--page);
    font-family: "Arimo", Arial, sans-serif;
  }
  .canvas {
    position: relative;
    width: 1200px;
    height: 1200px;
  }
  .card {
    position: absolute;
    width: 640px;
    height: 390px;
    overflow: hidden;
    box-shadow: 0 6px 18px rgba(0,0,0,0.18);
  }
  .card-front {
    left: 80px;
    top: 230px;
    background: var(--card-white);
    z-index: 2;
  }
  .card-back {
    left: 480px;
    top: 580px;
    background: var(--card-black);
    z-index: 1;
  }
  .front-shapes {
    position: absolute;
    inset: 0;
  }
  .brand {
    position: absolute;
    display: flex;
    align-items: center;
    gap: 10px;
  }
  .brand-mark {
    width: 16px;
    height: 16px;
    background: var(--brand-green);
    flex: none;
  }
  .brand-name {
    color: var(--brand-grey);
    font-weight: 700;
    font-size: 22px;
    line-height: 1.1;
    letter-spacing: 0.5px;
  }
  .card-front .brand {
    left: 38px;
    top: 150px;
    width: 160px;
  }
  .contact {
    position: absolute;
    right: 40px;
    top: 78px;
    text-align: right;
    color: var(--text-light);
  }
  .contact-name {
    font-size: 26px;
    margin: 0;
    font-weight: 400;
  }
  .contact-title {
    font-size: 15px;
    font-style: italic;
    color: var(--text-soft);
    margin: 4px 0 14px;
  }
  .contact-line {
    font-size: 14px;
    margin: 2px 0;
    color: var(--text-soft);
  }
  .address {
    position: absolute;
    left: 300px;
    bottom: 60px;
    color: var(--text-soft);
    font-size: 13px;
    line-height: 1.45;
  }
  .address-label {
    display: inline-block;
    width: 118px;
  }
  .card-back .brand {
    left: 0;
    right: 0;
    top: 140px;
    justify-content: center;
  }
  .card-back .brand-name {
    font-size: 28px;
  }
  .website {
    position: absolute;
    left: 0;
    right: 0;
    top: 210px;
    text-align: center;
    color: var(--text-soft);
    font-size: 15px;
    letter-spacing: 7px;
  }
</style>
</head>
<body>
<main class="canvas">
  <section class="card card-front" aria-label="Business card front">
    <svg class="front-shapes" width="640" height="390" viewBox="0 0 640 390" aria-hidden="true">
      <path class="accent-chevron" fill="var(--accent-red)"
            d="M300 0 C 250 70, 215 160, 175 300 L 0 240 L 0 262 L 130 390 L 215 390 Z"/>
      <path class="dark-panel" fill="var(--card-black)"
            d="M305 0 L 640 0 L 640 390 L 215 390 C 235 250, 255 110, 305 0 Z"/>
    </svg>

    <div class="brand">
      <span class="brand-mark"></span>
      <span class="brand-name">Harlow Ironworks</span>
    </div>

    <div class="contact">
      <h1 class="contact-name">Marcus Reilly</h1>
      <p class="contact-title">Chairman</p>
      <p class="contact-line">Phone: 0418 539 746 and (02) 6193 4827</p>
      <p class="contact-line">email: info@harlowiw.com.au</p>
    </div>

    <div class="address">
      <div><span class="address-label">address (2 lines) .</span>xxxxxxxxxxxxxxxxxxxxxxxx</div>
      <div><span class="address-label">address (2 lines)</span>xxxxxxxxxxxxxxxxxxxxxxxx</div>
    </div>
  </section>

  <section class="card card-back" aria-label="Business card back">
    <div class="brand">
      <span class="brand-mark"></span>
      <span class="brand-name">Harlow Ironworks</span>
    </div>
    <p class="website">www.harlowiw.com.au</p>
  </section>
</main>
</body>
</html>
```